Tarvel Ridge LLC

Need Professional Business cards for New Investment Fund

Target Market(s)

High Quality investors

Industry/Entity Type

Financial

Contact Information for Business Card

Phone Number +1 555 284 6193
Name Pavel Orlinsky
Title Fund Manager
email po@FundTarvel.example
Website www.FundTarvel.example

Colors

Designer to choose colors to be used in the design.

Requirements
Must have
• Must have our Logo and all of the above. Must be made so lettering and loge can be raised

```html
<!DOCTYPE html>
<html lang="en">
<head>
<meta charset="utf-8">
<title>Tarvel Ridge LLC – Business Card</title>
<link href="https://fonts.googleapis.com/css2?family=Montserrat:wght@400;500&display=swap" rel="stylesheet">
<style>
  :root {
    --backdrop: #d6d6d6;
    --card-dark: #46503f;
    --card-light: #ffffff;
    --accent-green: #5cc244;
    --brand-green: #86d66f;
    --ink-grey: #5a5a5a;
    --ink-dark: #3c3c3c;
  }
  * { box-sizing: border-box; margin: 0; padding: 0; }
  html, body {
    width: 1200px; height: 900px; overflow: hidden;
    background: var(--backdrop);
    font-family: "Montserrat", Arial, sans-serif;
  }
  .card-set {
    position: absolute; inset: 0;
    display: flex; align-items: center; justify-content: center; gap: 40px;
  }
  .card {
    width: 525px; height: 300px;
    box-shadow: 0 6px 14px rgba(0,0,0,0.18);
    position: relative;
  }
  .card--front {
    background: var(--card-dark);
    display: flex; align-items: center; justify-content: center;
  }
  .brand-mark {
    display: flex; align-items: center; gap: 14px;
  }
  .brand-mark__square {
    width: 22px; height: 22px; background: var(--brand-green);
  }
  .brand-mark__name {
    color: var(--brand-green);
    font-weight: 500; font-size: 30px; letter-spacing: 3px;
    text-transform: uppercase;
  }
  .card--back {
    background: var(--card-light);
    display: flex; align-items: center; justify-content: center; gap: 22px;
    padding: 0 30px;
  }
  .holder { text-align: right; }
  .holder__name {
    color: var(--accent-green); font-weight: 500; font-size: 19px;
  }
  .holder__title {
    color: var(--ink-grey); font-weight: 400; font-size: 15px; margin-top: 3px;
  }
  .back-brand {
    color: var(--accent-green); font-weight: 500; font-size: 15px;
    letter-spacing: 1px; text-transform: uppercase;
    border-left: 1px solid #cfcfcf; border-right: 1px solid #cfcfcf;
    padding: 6px 14px;
  }
  .contact-list { list-style: none; }
  .contact-list li {
    display: flex; align-items: center; gap: 6px;
    color: var(--ink-dark); font-size: 13px; line-height: 21px;
  }
  .contact-list svg { width: 12px; height: 12px; flex: none; }
</style>
</head>
<body>
  <main class="card-set">
    <section class="card card--front" aria-label="Card front">
      <div class="brand-mark">
        <span class="brand-mark__square"></span>
        <span class="brand-mark__name">Tarvel Ridge</span>
      </div>
    </section>

    <section class="card card--back" aria-label="Card back">
      <div class="holder">
        <p class="holder__name">Pavel Orlinsky</p>
        <p class="holder__title">Fund Manager</p>
      </div>
      <div class="back-brand">Tarvel Ridge</div>
      <ul class="contact-list">
        <li>
          <svg viewBox="0 0 12 12"><path d="M3 1 L5 3.5 L4 4.8 Q5 7 7.2 8 L8.5 7 L11 9 L10 11 Q4 11 1 2 Z" fill="var(--accent-green)"/></svg>
          +1 555 284 6193
        </li>
        <li>
          <svg viewBox="0 0 12 12"><rect x="0.5" y="2" width="11" height="8" fill="var(--accent-green)"/><path d="M0.5 2 L6 6.5 L11.5 2" stroke="#fff" stroke-width="1.2" fill="none"/></svg>
          po@FundTarvel.example
        </li>
        <li>
          <svg viewBox="0 0 12 12"><circle cx="6" cy="6" r="5.5" fill="var(--accent-green)"/><path d="M0.5 6 H11.5 M6 0.5 Q3 6 6 11.5 M6 0.5 Q9 6 6 11.5" stroke="#fff" stroke-width="0.9" fill="none"/></svg>
          www.FundTarvel.example
        </li>
      </ul>
    </section>
  </main>
</body>
</html>
```